Website Design: Neuroscience research lab at an academic University.

I am looking to redo my University website for Neuroscience Research. <br/><br/>I am looking for a clean, modern and organized design to publish our work. Although I want a modern look, the focus should be on the text content.<br/><br/>Pages I need. These pages should be in the navigation bar;<br/>*Home*: with overview of the lab, contact information, and possibly with <br/>"Recent News and Events" information<br/>*Research*/Projects: will have text description, images, as well as video of various research projects we have done or are working on<br/>*People*: Personnel page with photos and bios of the team<br/>*Publications*: List of research articles with hyperlinks to online <br/>versions of articles as well as PDFs<br/>*News*: Continually updated list of events<br/><br/><br/>Some designs I like: <br/><br/>https://www.morvanlabs.example/<br/>http://www.quillarbor.example/<br/>https://tenwicklab.example<br/>http://www.galdrenlab.example/<br/>https://vqom.halbrook.example/

Target Market(s)

Academics, university students, government

Logo Text

Pellory Lab

Number of Pages Required

5+ page

Colors

Designer to choose colors to be used in the design.

Requirements
Must have
• A modern but elegant design that focuses on the research but that is also visually appealing.
• For the logo, please see the sketch in the attached files. That is a rough sketch of a logo that you can base your logo design on.
Should not have
• No search bar

```html
<!DOCTYPE html>
<html lang="en">
<head>
<meta charset="utf-8">
<title>Pellory Lab – Neuroscience Research Lab</title>
<link href="https://fonts.googleapis.com/css2?family=Lato:wght@400;700&family=Oswald:wght@600&display=swap" rel="stylesheet">
<style>
:root{
  --orange:#ff4a12;
  --navy:#1b3a9a;
  --teal:#1a8fc4;
  --green:#3b8b2d;
  --gold:#d9a31a;
  --purple:#6b2bb0;
  --ink:#2b2b2b;
  --text:#4a4a4a;
  --soft:#f3f3f3;
  --dark:#1f1f21;
  --white:#ffffff;
}
*{box-sizing:border-box;margin:0;padding:0}
html,body{width:1200px;height:3600px;overflow:hidden}
body{position:relative;background:var(--soft);font-family:'Lato',sans-serif;color:var(--text)}
.abs{position:absolute}
/* header */
.site-header{left:0;top:0;width:1200px;height:95px;background:var(--white);z-index:3}
.brand{left:75px;top:28px;display:flex;align-items:center;gap:10px;font-weight:700;font-size:22px;color:var(--ink)}
.brand-dot{width:26px;height:26px;border-radius:50%;background:var(--orange)}
.main-nav{left:282px;top:41px;display:flex;gap:38px;font-size:15px;color:#333}
.main-nav a{color:inherit;text-decoration:none}
.main-nav .active{color:var(--navy)}
/* hero */
.hero{left:0;top:95px;width:1200px;height:710px;background:radial-gradient(circle at 75% 40%,#2a6fd6 0%,#123a8c 30%,#0a1a4a 65%,#06102e 100%)}
.hero-title{left:0;top:318px;width:1200px;text-align:center;font-family:'Oswald',sans-serif;font-size:118px;line-height:1;color:var(--white);letter-spacing:1px}
.hero-sub{left:0;top:448px;width:1200px;text-align:center;font-weight:700;font-size:31px;color:var(--white)}
.btn{display:block;width:180px;height:53px;line-height:53px;border-radius:27px;background:var(--orange);color:var(--white);font-weight:700;font-size:18px;text-align:center;text-decoration:none}
.hero-btn{left:510px;top:510px}
.dots{left:556px;top:730px;display:flex;gap:12px}
.dots span{width:13px;height:13px;border-radius:50%;background:var(--orange)}
.dots span:first-child{background:var(--white)}
/* headings */
.section-title{left:0;width:1200px;text-align:center;font-size:32px;font-weight:700;color:var(--ink)}
.rule{left:550px;width:100px;height:4px;background:var(--navy)}
.intro{left:150px;top:955px;width:900px;text-align:center;font-size:16px;line-height:32.5px}
.intro-btn{left:510px;top:1124px}
/* features */
.feature-photo{left:74px;top:1407px;width:422px;height:493px;border-radius:18px;background:linear-gradient(135deg,#d9e2ea,#f4f6f8 45%,#b9c9d8)}
.feature{left:524px;width:602px;height:151px;border-radius:20px;background:var(--soft)}
.feature.raised{background:var(--white);box-shadow:0 4px 14px rgba(0,0,0,.18)}
.feature svg{position:absolute;left:22px;top:26px}
.feature h3{position:absolute;left:128px;top:14px;font-size:24px;color:var(--green);font-weight:700}
.feature p{position:absolute;left:128px;top:55px;width:450px;font-size:16px;line-height:27px}
/* news */
.news-card{width:331px}
.news-img{width:331px;height:200px;border-radius:18px}
.date{font-size:15px;color:var(--gold);margin-top:24px}
.news-card h4{font-size:19px;color:var(--teal);margin-top:7px;font-weight:700}
.news-card p{font-size:16px;line-height:27px;margin-top:8px;width:320px}
.more{display:block;margin-top:14px;font-size:14px;font-weight:700;color:var(--ink);text-decoration:none}
/* latest */
.latest{background:var(--white);border-radius:18px;box-shadow:0 3px 12px rgba(0,0,0,.15);overflow:hidden}
.latest .pic{height:262px}
.latest .body{padding:26px 24px}
.latest .d{font-size:15px;color:var(--gold)}
.latest h5{font-size:17px;line-height:27px;color:var(--ink);font-weight:700;margin-top:6px}
.latest .rm{font-size:14px;font-weight:700;color:var(--orange);margin-top:6px;display:block;text-decoration:none}
.overlay-card{left:794px;width:332px;height:198px;border-radius:18px;overflow:hidden}
.overlay-card .cap{position:absolute;left:24px;bottom:28px;color:var(--white);font-size:17px;font-weight:700;line-height:25px}
.overlay-card .cap span{display:block;color:var(--gold);font-size:15px;font-weight:400}
/* footer */
.footer-nav{left:0;top:3444px;width:1200px;display:flex;justify-content:center;gap:48px;font-size:15px;color:var(--white)}
.copyright{left:0;top:3488px;width:1200px;text-align:center;font-size:14px;color:#ddd}
.social{left:478px;top:3526px;display:flex;gap:28px}
.social span{width:26px;height:26px;border-radius:50%;background:var(--white)}
</style>
</head>
<body>
<header class="site-header abs">
  <div class="brand abs"><span class="brand-dot"></span>Pellory Lab</div>
  <nav class="main-nav abs">
    <a class="active" href="#">HOME</a><a href="#">RECENT NEWS AND EVENTS</a><a href="#">RESEARCH</a><a href="#">PEOPLE</a><a href="#">PUBLICATIONS</a><a href="#">NEWS</a><a href="#">CONTACT</a>
  </nav>
</header>

<section class="hero abs" role="img" aria-label="Glowing blue neurons network"></section>
<svg class="abs" style="left:0;top:700px" width="1200" height="110" viewBox="0 0 1200 110" aria-hidden="true"><path d="M0 12 Q600 200 1200 12 V110 H0 Z" fill="var(--soft)"/></svg>
<h1 class="hero-title abs">PELLORY LAB</h1>
<p class="hero-sub abs">NEUROSCIENCE RESEARCH LAB</p>
<a class="btn hero-btn abs" href="#">READ MORE</a>
<div class="dots abs"><span></span><span></span><span></span><span></span></div>

<h2 class="section-title abs" style="top:874px">WELCOME TO OUR LAB</h2>
<div class="rule abs" style="top:932px"></div>
<p class="intro abs">Lorem ipsum dolor sit amet, consectetur adipiscing elit. Proin facilisis luctus nisl at maximus.<br>Proin in molestie massa. Cras feugiat molestie ultricies. Proin tristique neque metus. Donec cursus leo nibh, in accumsan diam pharetra id. Aenean felis dolor, convallis et dui id, fringilla ultrices neque. Class aptent taciti sociosqu ad litora torquent per conubia nostra, per inceptos himenaeos.</p>
<a class="btn intro-btn abs" href="#">READ MORE</a>

<svg class="abs" style="left:0;top:1255px" width="1200" height="760" viewBox="0 0 1200 760" aria-hidden="true"><path d="M0 92 Q600 -60 1200 92 V760 H0 Z" fill="var(--white)"/></svg>
<div class="feature-photo abs" role="img" aria-label="Scientist in lab coat using a pipette"></div>

<article class="feature raised abs" style="top:1407px">
  <svg width="80" height="80" viewBox="0 0 80 80" aria-hidden="true"><circle cx="40" cy="18" r="10" fill="var(--navy)"/><rect x="24" y="32" width="32" height="26" rx="6" fill="var(--navy)"/><rect x="18" y="60" width="44" height="8" fill="var(--navy)"/></svg>
  <h3>Research</h3>
  <p>Lorem ipsum dolor sit amet, consectetur adipiscing elit. Proin facilisis luctus nisl at maximus in molestie massa. Cras feugiat molestie ultricies.</p>
</article>
<article class="feature abs" style="top:1580px">
  <svg width="96" height="80" viewBox="0 0 96 80" aria-hidden="true"><g fill="var(--purple)"><circle cx="48" cy="18" r="11"/><circle cx="24" cy="26" r="9"/><circle cx="72" cy="26" r="9"/><path d="M30 70 Q30 36 48 36 Q66 36 66 70Z"/><path d="M8 64 Q8 40 24 40 Q34 40 36 52 L30 64Z"/><path d="M88 64 Q88 40 72 40 Q62 40 60 52 L66 64Z"/></g></svg>
  <h3>People</h3>
  <p>Lorem ipsum dolor sit amet, consectetur adipiscing elit. Proin facilisis luctus nisl at maximus in molestie massa. Cras feugiat molestie ultricies.</p>
</article>
<article class="feature abs" style="top:1750px">
  <svg width="80" height="80" viewBox="0 0 80 80" aria-hidden="true"><g fill="none" stroke="var(--purple)" stroke-width="4"><rect x="18" y="6" width="56" height="68" rx="3"/><path d="M18 34 H6 V70 Q6 74 12 74 H18"/></g><g fill="var(--navy)"><rect x="26" y="16" width="40" height="10"/><rect x="26" y="34" width="16" height="14"/><rect x="48" y="34" width="18" height="4"/><rect x="48" y="44" width="18" height="4"/><rect x="26" y="56" width="40" height="4"/></g></svg>
  <h3>Publications</h3>
  <p>Lorem ipsum dolor sit amet, consectetur adipiscing elit. Proin facilisis luctus nisl at maximus in molestie massa. Cras feugiat molestie ultricies.</p>
</article>

<svg class="abs" style="left:0;top:1970px" width="1200" height="100" viewBox="0 0 1200 100" aria-hidden="true"><path d="M0 95 Q600 -60 1200 95 V100 H0 Z" fill="var(--soft)"/></svg>
<h2 class="section-title abs" style="top:2088px">RECENT NEWS AND EVENTS</h2>
<div class="rule abs" style="top:2146px"></div>

<article class="news-card abs" style="left:74px;top:2203px">
  <div class="news-img" role="img" aria-label="Researcher at a microscope in a blue-lit lab" style="background:linear-gradient(135deg,#0e2f74,#2d6ac4 60%,#9ab9dc)"></div>
  <div class="date">DEC 10, 2019</div><h4>LOREM IPSUM DOLOR SIT AMET</h4>
  <p>Consectetur adipiscing elit. Proin facilisis luctus nisl at maximu maximus ante consequat est interdum.</p><a class="more" href="#">READ MORE ››</a>
</article>
<article class="news-card abs" style="left:436px;top:2203px">
  <div class="news-img" role="img" aria-label="Doctor holding a glowing holographic brain model" style="background:linear-gradient(135deg,#6c8fb8,#a9c4dc 50%,#3d6fa6)"></div>
  <div class="date">DEC 10, 2019</div><h4>LOREM IPSUM DOLOR SIT AMET</h4>
  <p>Consectetur adipiscing elit. Proin facilisis luctus nisl at maximu maximus ante consequat est interdum.</p><a class="more" href="#">READ MORE ››</a>
</article>
<article class="news-card abs" style="left:796px;top:2203px">
  <div class="news-img" role="img" aria-label="Scientists reviewing brain scans on monitors" style="background:linear-gradient(135deg,#1c2e52,#5a7aa6 55%,#c9d6e6)"></div>
  <div class="date">DEC 10, 2019</div><h4>LOREM IPSUM DOLOR SIT AMET</h4>
  <p>Consectetur adipiscing elit. Proin facilisis luctus nisl at maximu maximus ante consequat est interdum.</p><a class="more" href="#">READ MORE ››</a>
</article>

<div class="abs" style="left:0;top:2680px;width:1200px;height:760px;background:var(--white)"></div>
<h2 class="section-title abs" style="top:2730px">LATEST NEWS</h2>
<div class="rule abs" style="top:2788px"></div>

<article class="latest abs" style="left:74px;top:2840px;width:422px;height:412px">
  <div class="pic" role="img" aria-label="Researchers with a patient wearing an EEG cap" style="background:linear-gradient(135deg,#1a3566,#6d8cb6 55%,#d8e2ee)"></div>
  <div class="body"><div class="d">DEC 10, 2019</div><h5>CURABITUR MAXIMUS ANTE CONSEQUAT EST INTERDUM NEC VOLUTPAT</h5><a class="rm" href="#">READ MORE ››</a></div>
</article>
<article class="latest abs" style="left:510px;top:2840px;width:270px;height:412px">
  <div class="pic" role="img" aria-label="Microscopic cells and virus particles" style="background:radial-gradient(circle at 50% 55%,#3aa8b8,#0d3a4e 45%,#6e0f1c 100%)"></div>
  <div class="body"><div class="d">DEC 10, 2019</div><h5>CURABITUR MAXIMUS ANTE CONSEQUAT EST</h5><a class="rm" href="#">READ MORE ››</a></div>
</article>
<article class="overlay-card abs" style="top:2840px" role="img" aria-label="Abstract dark blue neural network">
  <div style="position:absolute;inset:0;background:linear-gradient(135deg,#0a1242,#2a3a9a 60%,#121a55)"></div>
  <div class="cap"><span>DEC 10, 2019</span>CURABITUR MAXIMUS<br>ANTE CONSEQUAT EST INTERDUM</div>
</article>
<article class="overlay-card abs" style="top:3055px" role="img" aria-label="Scientist studying brain scans on screens">
  <div style="position:absolute;inset:0;background:linear-gradient(135deg,#39455c,#1d2b44 55%,#0e1526)"></div>
  <div class="cap"><span>DEC 10, 2019</span>CURABITUR MAXIMUS<br>ANTE CONSEQUAT EST INTERDUM</div>
</article>

<svg class="abs" style="left:0;top:3330px" width="1200" height="270" viewBox="0 0 1200 270" aria-hidden="true"><path d="M0 92 Q600 -90 1200 92 V270 H0 Z" fill="var(--dark)"/></svg>
<nav class="footer-nav abs"><span>HOME</span><span>RECENT NEWS AND EVENTS</span><span>RESEARCH</span><span>PEOPLE</span><span>PUBLICATIONS</span><span>NEWS</span><span>CONTACT</span></nav>
<p class="copyright abs">Copyright ©2019 CompanyName.All Rights Reserved.</p>
<div class="social abs" aria-label="Social links"><span></span><span></span><span></span><span></span><span></span></div>
</body>
</html>
```